Personal Injury Billboard for a law frim

Our firm has a billboard we need art for. It will specifically for personal injury cases. The dimensions of art the billboard are 9 ft high 29 feet wide.

We want to highlight the terms, "Serious Injuries" and "Trusted. Local. Experienced." We want to incorporate the attached "Vantor Advocates" badge as well as our attached firm logo. We want the blue color scheme (see attached).

Maybe an image of an industrial plant in the background?

Font styles to use
Sans Serif

Colors

Designer to choose colors to be used in the design.

```html
<!DOCTYPE html>
<html lang="en">
<head>
<meta charset="UTF-8">
<title>Halden Ross Merritt – Serious Injuries Billboard</title>
<link href="https://fonts.googleapis.com/css2?family=League+Gothic&family=Oswald:wght@600&family=Poppins:wght@400;500;600&display=swap" rel="stylesheet">
<style>
  :root {
    --page-bg: #e9eaec;
    --panel-white: #ffffff;
    --blue-deep: #123a78;
    --blue-mid: #2c64a8;
    --blue-light: #3f8fd4;
    --blue-steel: #5f8fc0;
    --navy-bar: #0f2a66;
    --text-white: #ffffff;
    --text-dark: #141a26;
    --link-blue: #1f56b8;
  }
  * { box-sizing: border-box; margin: 0; padding: 0; }
  html, body {
    width: 1200px;
    height: 800px;
    overflow: hidden;
    background: var(--page-bg);
  }
  .billboard {
    position: absolute;
    left: 30px;
    top: 193px;
    width: 1140px;
    height: 414px;
    display: flex;
    box-shadow: 0 6px 18px rgba(0,0,0,0.18);
  }
  .brand-panel {
    width: 352px;
    height: 100%;
    background: var(--panel-white);
    display: flex;
    flex-direction: column;
    align-items: center;
    justify-content: center;
    font-family: "Poppins", sans-serif;
  }
  .brand-mark {
    width: 64px;
    height: 64px;
    background: var(--blue-mid);
    margin-bottom: 14px;
  }
  .brand-name {
    font-weight: 600;
    font-size: 24px;
    letter-spacing: 1px;
    color: var(--blue-deep);
    margin-bottom: 8px;
  }
  .brand-url {
    font-size: 14px;
    font-weight: 400;
    color: var(--link-blue);
    text-decoration: underline;
    margin-bottom: 4px;
  }
  .brand-firm {
    font-size: 15px;
    font-weight: 600;
    color: var(--text-dark);
    letter-spacing: 0.3px;
  }
  .brand-role {
    display: flex;
    align-items: center;
    gap: 6px;
    font-size: 9px;
    font-weight: 500;
    letter-spacing: 1px;
    color: var(--text-dark);
    margin-top: 1px;
  }
  .brand-role::before,
  .brand-role::after {
    content: "";
    width: 74px;
    height: 1.5px;
    background: var(--text-dark);
  }
  .message-panel {
    position: relative;
    flex: 1;
    height: 100%;
    overflow: hidden;
  }
  .industrial-backdrop {
    position: absolute;
    inset: 0;
    background: linear-gradient(180deg, var(--blue-deep) 0%, var(--blue-mid) 55%, var(--blue-steel) 100%);
  }
  .headline {
    position: absolute;
    left: 0;
    right: 0;
    top: 98px;
    text-align: center;
    font-family: "League Gothic", sans-serif;
    font-size: 150px;
    line-height: 1;
    letter-spacing: 1px;
    color: var(--text-white);
    text-shadow: 3px 4px 6px rgba(0,0,0,0.35);
  }
  .tagline {
    position: absolute;
    left: 74px;
    width: 672px;
    top: 241px;
    height: 62px;
    background: var(--blue-light);
    border: 1px solid rgba(255,255,255,0.35);
    display: flex;
    align-items: center;
    justify-content: center;
    font-family: "Oswald", sans-serif;
    font-weight: 600;
    font-size: 44px;
    letter-spacing: 0.5px;
    color: var(--text-white);
  }
  .contact-bar {
    position: absolute;
    left: 0;
    right: 0;
    bottom: 0;
    height: 26px;
    background: var(--navy-bar);
    display: flex;
    align-items: center;
    justify-content: flex-end;
    gap: 22px;
    padding-right: 28px;
    font-family: "Poppins", sans-serif;
    font-size: 14px;
    color: var(--text-white);
  }
  .contact-label { font-weight: 600; margin-right: 6px; }
  .contact-value { font-weight: 400; }
</style>
</head>
<body>
  <main class="billboard">
    <section class="brand-panel">
      <div class="brand-mark"></div>
      <div class="brand-name">HRM</div>
      <div class="brand-url">www.hrm-law.com</div>
      <div class="brand-firm">HALDEN ROSS MERRITT</div>
      <div class="brand-role">ATTORNEYS</div>
    </section>
    <section class="message-panel">
      <div class="industrial-backdrop" role="img" aria-label="Industrial plant with smokestacks and factory buildings under an overcast sky, tinted blue"></div>
      <h1 class="headline">SERIOUS INJURIES</h1>
      <div class="tagline">TRUSTED. LOCAL. EXPERIENCED</div>
      <div class="contact-bar">
        <span><span class="contact-label">Production Contact:</span><span class="contact-value">jtorres@brightlinemedia.com</span></span>
        <span><span class="contact-label">Media Contact:</span><span class="contact-value">kellis@brightlinemedia.com</span></span>
      </div>
    </section>
  </main>
</body>
</html>
```